New Television Homescreen Template

We need a new default homescreen design for our televisions. This should reflect our company branding. My company is called Wardline Systems, WLS for short. Our website is www.wlsx.example. We develop televisions and infotainment solutions for the healthcare industry. I am somewhat open to different color palettes but our company colors are blue, black, and white. Our design is constrained by the 9 buttons, however the design of the buttons can be changed. Also, there is a video box on the right side of the screen as shown, this design can also be changed.

Target Market(s)

Hospital Patients

Requirements
Must have
• PSD template.

```html
<!DOCTYPE html>
<html lang="en">
<head>
<meta charset="utf-8">
<title>Wardline Systems — TV Homescreen</title>
<link rel="stylesheet" href="https://fonts.googleapis.com/css2?family=Lora:wght@600;700&display=swap">
<style>
  :root {
    --bg-teal: #a9d4da;
    --bg-glow: #a6cdf4;
    --tile-blue: #5585b8;
    --tile-text: #121418;
    --brand-ink: #0c0d10;
    --brand-mark: #3a52cf;
    --tagline: #f4f8fa;
    --frame-top: #ffffff;
    --frame-bottom: #627086;
    --screen: #eff3f6;
    --band-top: #f0f3f5;
    --band-bottom: #4aa6b8;
  }
  * { margin: 0; padding: 0; box-sizing: border-box; }
  html, body { width: 1200px; height: 675px; overflow: hidden; }
  body { font-family: "Lora", Georgia, serif; }

  .homescreen {
    position: relative;
    width: 1200px;
    height: 675px;
    overflow: hidden;
    background:
      radial-gradient(ellipse 340px 200px at 880px 530px, var(--bg-glow) 0%, rgba(166,205,244,0) 100%),
      linear-gradient(100deg, var(--bg-teal) 0%, #a8d3dc 55%, #a6d0e6 100%);
  }

  .brand {
    position: absolute;
    left: 686px;
    top: 40px;
    display: flex;
    align-items: center;
    gap: 14px;
  }
  .brand-mark {
    width: 18px;
    height: 18px;
    background: var(--brand-mark);
  }
  .brand-name {
    font-weight: 700;
    font-size: 38px;
    line-height: 1;
    color: var(--brand-ink);
    letter-spacing: 0.2px;
  }
  .brand-tagline {
    position: absolute;
    left: 835px;
    top: 100px;
    font-weight: 600;
    font-size: 23px;
    color: var(--tagline);
    letter-spacing: 0.3px;
  }

  .channel-grid {
    position: absolute;
    left: 27px;
    top: 190px;
    display: grid;
    grid-template-columns: repeat(3, 176px);
    grid-template-rows: repeat(3, 88px);
    column-gap: 17px;
    row-gap: 30px;
  }
  .channel-tile {
    display: flex;
    align-items: center;
    justify-content: center;
    background: var(--tile-blue);
    border-radius: 10px;
    color: var(--tile-text);
    font-weight: 700;
    font-size: 25px;
  }

  .video-frame {
    position: absolute;
    left: 728px;
    top: 234px;
    width: 395px;
    height: 263px;
    border-radius: 10px;
    background: linear-gradient(180deg, var(--frame-top) 0%, #dfe3e8 30%, var(--frame-bottom) 100%);
  }
  .video-screen {
    position: absolute;
    left: 22px;
    top: 17px;
    width: 351px;
    height: 220px;
    border-radius: 9px;
    background: var(--screen);
  }

  .footer-band {
    position: absolute;
    left: 0;
    bottom: 0;
    width: 1200px;
    height: 122px;
    background: linear-gradient(180deg, var(--band-top) 0%, #c9e2e6 35%, var(--band-bottom) 100%);
  }
</style>
</head>
<body>
  <main class="homescreen">
    <header>
      <div class="brand">
        <span class="brand-mark"></span>
        <span class="brand-name">Wardline Systems</span>
      </div>
      <p class="brand-tagline">improving patient care</p>
    </header>

    <nav class="channel-grid">
      <div class="channel-tile">Cable TV</div>
      <div class="channel-tile">Cable TV</div>
      <div class="channel-tile">Cable TV</div>
      <div class="channel-tile">Cable TV</div>
      <div class="channel-tile">Cable TV</div>
      <div class="channel-tile">Cable TV</div>
      <div class="channel-tile">Cable TV</div>
      <div class="channel-tile">Cable TV</div>
      <div class="channel-tile">Cable TV</div>
    </nav>

    <section class="video-frame" aria-label="Video preview">
      <div class="video-screen"></div>
    </section>

    <footer class="footer-band"></footer>
  </main>
</body>
</html>
```